Welcome Postcard for existing church in new facility

I need a postcard to express the 4 strong points of our ministry. I have attached a sample postcard that we really liked as a start point. Our four strengths are;

LOVE
WORSHIP
DIVERSITY
DOCTRINE

I want to make sure the colors used are vivid and provide plenty of pop.

I have provide images to coincide with the four ministry strengths and they are named according the the strength the coincide with, pick whichever you think is best graphically.

our twitter handle is @BRAVOHOPETX
our FB handle is /BRAVOHOPETX
our Youtube handle is /GraceHarbored

I must have all PSD layers in case last minutes changes need to be made. THIS IS A REQUIREMENT.
Updates

Project Deadline Extended
Reason: Not enough options being proposed yet

Target Market(s)

General Population

Industry/Entity Type

Non-Profit

Font styles to use
Sans Serif

Requirements
Must have
• I must have all PSD layers in case last minutes changes need to be made. THIS IS A REQUIREMENT.
Nice to have
• Be attractive and market friendly is US marketplace
Should not have
• Please do not submit multiple designs with slight deviations. If you submit multiple designs please make them totally different one from another. We will not consider your design if you spam us.

```html
<!DOCTYPE html>
<html lang="en">
<head>
<meta charset="utf-8">
<title>Bravo Hope Ministries – Welcome Postcard</title>
<link href="https://fonts.googleapis.com/css2?family=Montserrat:wght@300;400;500;600&display=swap" rel="stylesheet">
<style>
  :root {
    --ink: #050505;
    --paper: #e9e7e3;
    --white: #ffffff;
    --brand-blue: #2a8fd0;
    --web-blue: #2b7fc2;
    --love-a: #e8318f;
    --love-b: #c85fb4;
    --worship-a: #a97d33;
    --worship-b: #f6a83b;
    --worship-c: #ef612b;
    --diversity-a: #2aa548;
    --diversity-b: #3cb64a;
    --diversity-c: #6cb94b;
    --doctrine-a: #3f8fc0;
    --doctrine-b: #1f86cf;
    --doctrine-c: #1379c9;
  }
  * { box-sizing: border-box; margin: 0; padding: 0; }
  html, body { width: 1200px; height: 900px; overflow: hidden; }
  body {
    background: var(--paper);
    font-family: "Montserrat", sans-serif;
    position: relative;
  }
  .postcard-frame {
    position: absolute;
    left: 270px; top: 20px;
    width: 660px; height: 860px;
    overflow: hidden;
    box-shadow: 0 6px 18px rgba(0,0,0,.25);
  }
  .postcard {
    position: absolute; left: 0; top: 0;
    width: 740px; height: 964px;
    background: var(--ink);
    transform: scale(0.8919);
    transform-origin: 0 0;
    color: var(--white);
  }
  .bands { position: absolute; inset: 0; width: 740px; height: 964px; }

  .masthead-mark {
    position: absolute; left: 44px; top: 24px;
    width: 70px; height: 70px;
    background: var(--brand-blue);
  }
  .masthead-name {
    position: absolute; left: 180px; top: 12px;
    font-weight: 300; font-size: 24px; line-height: 29px;
    color: var(--brand-blue);
  }
  .masthead-phone {
    position: absolute; right: 28px; top: 36px;
    font-weight: 600; font-size: 44px; line-height: 1;
    letter-spacing: .01em;
  }

  .pillar-word {
    position: absolute;
    font-weight: 500; font-size: 70px; line-height: 1;
    letter-spacing: -0.03em;
    white-space: nowrap;
    text-shadow: 0 1px 3px rgba(0,0,0,.2);
  }
  .pillar-note {
    position: absolute;
    font-weight: 400; font-size: 17px; line-height: 22px;
    white-space: nowrap;
  }
  .note-right { text-align: right; }

  .love-word { left: 48px; top: 172px; }
  .love-note { left: 258px; top: 180px; }
  .worship-word { left: 344px; top: 382px; }
  .worship-note { right: 424px; top: 389px; }
  .diversity-word { left: 48px; top: 585px; }
  .diversity-note { left: 432px; top: 591px; }
  .doctrine-word { left: 288px; top: 765px; }
  .doctrine-note { right: 476px; top: 774px; }

  .social-row {
    position: absolute; left: 24px; right: 28px; top: 898px;
    display: flex; justify-content: space-between; align-items: center;
  }
  .social-handle {
    display: flex; align-items: center; gap: 8px;
    font-weight: 600; font-size: 11px; letter-spacing: .01em;
  }
  .social-chip {
    width: 21px; height: 21px; border-radius: 3px;
    background: var(--brand-blue);
  }
  .web-address {
    position: absolute; left: 0; right: 0; top: 926px;
    text-align: center;
    font-weight: 400; font-size: 18px;
    letter-spacing: .42em;
    color: var(--web-blue);
  }
</style>
</head>
<body>
  <div class="postcard-frame">
    <div class="postcard">
      <svg class="bands" viewBox="0 0 740 964" xmlns="http://www.w3.org/2000/svg">
        <defs>
          <linearGradient id="love-fill" x1="0" y1="0" x2="1" y2="0">
            <stop offset="0" stop-color="var(--love-a)"/>
            <stop offset=".55" stop-color="#ec5ea6"/>
            <stop offset="1" stop-color="var(--love-b)"/>
          </linearGradient>
          <linearGradient id="worship-fill" x1="0" y1="0" x2="1" y2="0">
            <stop offset="0" stop-color="var(--worship-a)"/>
            <stop offset=".5" stop-color="#e0a23f"/>
            <stop offset=".75" stop-color="var(--worship-b)"/>
            <stop offset="1" stop-color="var(--worship-c)"/>
          </linearGradient>
          <linearGradient id="diversity-fill" x1="0" y1="0" x2="1" y2="0">
            <stop offset="0" stop-color="var(--diversity-a)"/>
            <stop offset=".45" stop-color="var(--diversity-b)"/>
            <stop offset="1" stop-color="var(--diversity-c)"/>
          </linearGradient>
          <linearGradient id="doctrine-fill" x1="0" y1="0" x2="1" y2="0">
            <stop offset="0" stop-color="var(--doctrine-a)"/>
            <stop offset=".5" stop-color="var(--doctrine-b)"/>
            <stop offset="1" stop-color="var(--doctrine-c)"/>
          </linearGradient>
        </defs>
        <polygon role="img" aria-label="Photo of two women embracing, tinted magenta"
                 points="0,128 740,88 740,313 0,277" fill="url(#love-fill)"/>
        <polygon role="img" aria-label="Photo of a worship service with a keyboard player, tinted orange"
                 points="0,283 740,321 740,480 0,532" fill="url(#worship-fill)"/>
        <polygon role="img" aria-label="Photo of a congregation praying together, tinted green"
                 points="0,538 740,487 740,719 0,690" fill="url(#diversity-fill)"/>
        <polygon role="img" aria-label="Photo of an open Bible, tinted blue"
                 points="0,687 740,726 740,879 0,879" fill="url(#doctrine-fill)"/>
      </svg>

      <div class="masthead-mark"></div>
      <div class="masthead-name">Bravo<br>Hope<br>Ministries</div>
      <div class="masthead-phone">(800) 555-0142</div>

      <div class="pillar-word love-word">LOVE</div>
      <div class="pillar-note love-note">Not simply a feeling, but<br>a decision and a commitment.</div>

      <div class="pillar-note note-right worship-note">The natural reaction to the<br>very presence of the Lord.</div>
      <div class="pillar-word worship-word">WORSHIP</div>

      <div class="pillar-word diversity-word">DIVERSITY</div>
      <div class="pillar-note diversity-note">Unique individuals,<br>making up one unified body.</div>

      <div class="pillar-note note-right doctrine-note">The expression of<br>a fundamental truth.</div>
      <div class="pillar-word doctrine-word">DOCTRINE</div>

      <div class="social-row">
        <div class="social-handle"><span class="social-chip"></span>/BRAVOHOPETX</div>
        <div class="social-handle"><span class="social-chip"></span>@BRAVOHOPETX</div>
        <div class="social-handle"><span class="social-chip"></span>/GraceHarbored</div>
      </div>
      <div class="web-address">bravohope.org</div>
    </div>
  </div>
</body>
</html>
```